Driving School Business card design

Hi, we are starting a new business (Driving School) and would like your help with our business card design.
We are located in Adelaide SA.
Our aim is to help young people achieve best possible results by promoting safe and stress free driving.

Name of our school is "Velmira" which means best or most favorable.

Hope there is someone out there in wonderful world of design who can think outside of square and give us recognizable/ unique business card design.

Target Market(s)

16+

Industry/Entity Type

Business

Contact Information for Business Card

Name of our business is "Velmira driver training"
Our idea is to make letter "L' in Velmira more distinct (noticeable) by different color or font, so it gets associated with learner driver.
We like combination of white, dark gray and yellow but do not limit our self to that.
Reverse side of our card would have to incorporate writing space for date and time of the next lesson.

Requirements
Must have
• Business name: Velmira driver training
• Owner/ instructor name
• Mobile no:
• Chatterloop logo
Should not have
• Anything Not associated with driving

```html
<!DOCTYPE html>
<html lang="en">
<head>
<meta charset="utf-8">
<title>Velmira Driver Training – Lesson Card</title>
<link rel="stylesheet" href="https://fonts.googleapis.com/css2?family=Open+Sans:ital,wght@0,400;1,800&display=swap">
<style>
  :root {
    --sea-light: #3cc3cf;
    --sea-deep: #1b9fb3;
    --coast-green: #4f6b3a;
    --coast-sand: #a3906a;
    --cliff-grey: #5d5a50;
    --plate-yellow: #f5f21f;
    --ink: #000000;
    --paper: #ffffff;
    --header-text: #f3ea00;
  }
  html, body {
    margin: 0;
    padding: 0;
    overflow: hidden;
    background: #ffffff;
  }
  .card {
    position: relative;
    width: 1200px;
    height: 763px;
    overflow: hidden;
    font-family: "Open Sans", Arial, sans-serif;
  }
  .card__scenery {
    position: absolute;
    inset: 0;
    background:
      linear-gradient(90deg, rgba(60,70,45,0.55) 0%, rgba(60,70,45,0) 9%, rgba(60,70,45,0) 80%, rgba(80,75,60,0.75) 92%),
      linear-gradient(180deg, var(--sea-deep) 0%, var(--sea-light) 30%, var(--sea-deep) 42%, var(--coast-green) 62%, var(--coast-sand) 86%, var(--cliff-grey) 100%);
  }
  .card__title {
    position: absolute;
    left: 146px;
    top: 96px;
    margin: 0;
    font-size: 52px;
    font-weight: 800;
    font-style: italic;
    color: var(--paper);
    letter-spacing: -0.5px;
    line-height: 1;
  }
  .learner-plate {
    position: absolute;
    left: 898px;
    top: 46px;
    width: 166px;
    height: 166px;
  }
  .lesson-table {
    position: absolute;
    left: 93px;
    top: 228px;
    width: 1028px;
    height: 445px;
    box-sizing: border-box;
    display: grid;
    grid-template-columns: 375px 348px 1fr;
    grid-template-rows: 62px repeat(6, 1fr);
    gap: 4px;
    padding: 0 4px 4px;
    background: var(--ink);
  }
  .lesson-table__head {
    display: flex;
    align-items: center;
    justify-content: center;
    color: var(--header-text);
    font-size: 33px;
    font-weight: 400;
    padding-top: 2px;
  }
  .lesson-table__cell {
    background: var(--paper);
  }
</style>
</head>
<body>
  <main class="card">
    <div class="card__scenery" role="img" aria-label="Coastal road photograph: turquoise ocean above green coastal scrub and a cliff"></div>

    <h1 class="card__title">Velmira Driver Training</h1>

    <svg class="learner-plate" viewBox="0 0 166 166" aria-label="Learner plate">
      <polygon points="83,2 164,83 83,164 2,83" fill="var(--plate-yellow)"/>
      <text x="83" y="108" text-anchor="middle" font-family="Open Sans, Arial, sans-serif" font-weight="800" font-size="72" fill="var(--ink)">L</text>
    </svg>

    <section class="lesson-table" aria-label="Lesson schedule">
      <div class="lesson-table__head">Next lesson</div>
      <div class="lesson-table__head">Date</div>
      <div class="lesson-table__head">Time</div>

      <div class="lesson-table__cell"></div><div class="lesson-table__cell"></div><div class="lesson-table__cell"></div>
      <div class="lesson-table__cell"></div><div class="lesson-table__cell"></div><div class="lesson-table__cell"></div>
      <div class="lesson-table__cell"></div><div class="lesson-table__cell"></div><div class="lesson-table__cell"></div>
      <div class="lesson-table__cell"></div><div class="lesson-table__cell"></div><div class="lesson-table__cell"></div>
      <div class="lesson-table__cell"></div><div class="lesson-table__cell"></div><div class="lesson-table__cell"></div>
      <div class="lesson-table__cell"></div><div class="lesson-table__cell"></div><div class="lesson-table__cell"></div>
    </section>
  </main>
</body>
</html>
```